The most modern business card ever !!!

Our company call “Vantilo”. Vantilo is a technology company specialized in cruises solutions. Out main product is a platform to reserve cruises. This is a revolutionary platform that make easier to travel agencies and final users to reserve cruises across dozen companies like tarvik, welbi, dpv, hbt, etc..We are a “start up”, with a young team of developers and we want to transmit it.. For it, we want something different, a modern business card that represent cruises and technology.. When someone receive this card, this person should say: wowww this is different… this is modern… this is a cruise related company..
Contact Information for Business Card
Requirements
Must have
- diferent, modern
Should not have
- traditions business card

```html
<!DOCTYPE html>
<html lang="en">
<head>
<meta charset="UTF-8">
<title>Vantilo — Business Card</title>
<link rel="stylesheet" href="https://fonts.googleapis.com/css2?family=Exo+2:wght@500&family=Montserrat:wght@400;500&display=swap">
<style>
  :root {
    --backdrop: #111214;
    --card-top: #9c9c9e;
    --card-bottom: #7e7f81;
    --ink-light: #f4f5f6;
    --ink-soft: #e3e5e7;
    --accent: #2aa6d9;
    --ship-tone-a: rgba(255,255,255,0.20);
    --ship-tone-b: rgba(255,255,255,0.06);
  }
  html, body {
    margin: 0;
    padding: 0;
    width: 1200px;
    height: 1200px;
    overflow: hidden;
    background: var(--backdrop);
  }
  .canvas {
    position: relative;
    width: 1200px;
    height: 1200px;
    display: flex;
    align-items: center;
    justify-content: center;
  }
  .card {
    position: relative;
    width: 900px;
    height: 568px;
    border-radius: 26px;
    background: linear-gradient(160deg, var(--card-top), var(--card-bottom));
    overflow: hidden;
  }
  .ship-artwork {
    position: absolute;
    left: 410px;
    right: 0;
    top: 330px;
    bottom: 0;
    border-top-left-radius: 100% 100%;
    background: linear-gradient(150deg, var(--ship-tone-a), var(--ship-tone-b));
  }
  .brand-name {
    position: absolute;
    left: 60px;
    top: 44px;
    margin: 0;
    font-family: "Exo 2", sans-serif;
    font-weight: 500;
    font-size: 84px;
    letter-spacing: 2px;
    color: var(--ink-light);
    line-height: 1;
  }
  .holder {
    position: absolute;
    right: 60px;
    top: 205px;
    text-align: right;
    font-family: "Exo 2", sans-serif;
    font-weight: 500;
    color: var(--ink-light);
  }
  .holder-name {
    font-size: 38px;
    letter-spacing: 2px;
    line-height: 1.1;
  }
  .holder-title {
    font-size: 20px;
    letter-spacing: 1px;
  }
  .contact-list {
    position: absolute;
    left: 60px;
    top: 190px;
    margin: 0;
    padding: 0;
    list-style: none;
    font-family: "Montserrat", sans-serif;
    font-size: 19px;
    color: var(--ink-soft);
  }
  .contact-item {
    display: flex;
    align-items: flex-start;
    gap: 14px;
    margin-bottom: 16px;
    line-height: 1.3;
  }
  .contact-icon {
    width: 22px;
    height: 22px;
    flex: none;
    margin-top: 1px;
  }
</style>
</head>
<body>
<main class="canvas">
  <article class="card">
    <div class="ship-artwork" role="img" aria-label="Thin white outline drawing of a cruise ship bow rising toward the lower right corner"></div>

    <h1 class="brand-name">Vantilo</h1>

    <ul class="contact-list">
      <li class="contact-item">
        <svg class="contact-icon" viewBox="0 0 24 24" aria-hidden="true">
          <path fill="var(--accent)" d="M12 2a7 7 0 0 0-7 7c0 5 7 13 7 13s7-8 7-13a7 7 0 0 0-7-7zm0 9.5A2.5 2.5 0 1 1 12 6.5a2.5 2.5 0 0 1 0 5z"/>
        </svg>
        <span>Your Address Will Be Here<br>123, xyz 1122</span>
      </li>
      <li class="contact-item">
        <svg class="contact-icon" viewBox="0 0 24 24" aria-hidden="true">
          <path fill="var(--accent)" d="M6.6 10.8a15 15 0 0 0 6.6 6.6l2.2-2.2a1 1 0 0 1 1-.25 11.4 11.4 0 0 0 3.6.6 1 1 0 0 1 1 1V20a1 1 0 0 1-1 1A17 17 0 0 1 3 4a1 1 0 0 1 1-1h3.5a1 1 0 0 1 1 1c0 1.250.2 2.45.6 3.6a1 1 0 0 1-.25 1z"/>
        </svg>
        <span>000 0000 12345</span>
      </li>
      <li class="contact-item">
        <svg class="contact-icon" viewBox="0 0 24 24" aria-hidden="true">
          <rect x="6" y="2" width="12" height="20" rx="2" fill="none" stroke="var(--accent)" stroke-width="2"/>
          <circle cx="12" cy="18" r="1.2" fill="var(--accent)"/>
        </svg>
        <span>123 45 6666 77</span>
      </li>
      <li class="contact-item">
        <svg class="contact-icon" viewBox="0 0 24 24" aria-hidden="true">
          <rect x="2" y="5" width="20" height="14" rx="1.5" fill="var(--accent)"/>
          <path d="M3 6l9 7 9-7" fill="none" stroke="#e8f6fc" stroke-width="1.6"/>
        </svg>
        <span>info@youremail.com</span>
      </li>
    </ul>

    <div class="holder">
      <div class="holder-name">Your Name</div>
      <div class="holder-title">Title</div>
    </div>
  </article>
</main>
</body>
</html>
```